Business Card Design Project

Brightwater Advisory is a newly created boutique consultancy focussing on delivering strategic consulting to medium and large businesses, with a focus on:
- Strategic planning and execution.
- Corporate function optimisation, especially in the areas of finance, commercial, and IT. This includes implementing the right functional design for the needs of the business, and ensuring the right skills.
- Performance management, in particular project governance and control, operational metrics and management reporting.
I have in mind a tag line for the business being:
"Helping business to discover sustainable value."
I am looking for a letterhead design which utilises my new logo on report templates (powerpoint and word), and letterhead.
Lexipoint defines a mother lode as follows:
"Mother lode is a principal vein or zone of veins of gold or silver ore. The term probably came from a literal translation of the Spanish veta madre, a term common in old Mexican mining. Veta madre, for instance, is the name given to an 11-kilometre-long (6.8 mi) silver vein discovered in 1548 in Guanajuato, New Spain (modern-day Mexico)."
My preference is for black and gold. Logo files are attached in .eps format. All fonts are outlined. The fonts that are used are "Crimson Text" and "Josefin Sans". They are free open source fonts and they are available here: http://www.typevault-demo.net/fonts
Target Market(s)
Medium to large corporates.
Industry/Entity Type
Boutique
Other font styles liked:
- All Fonts Are Outlined. The Fonts That Are Used Are "Crimson Text" And "Josefin Sans". They Are Free Open Source Fonts And They Are Available Here: Http://www.typevault-demo.net/fonts

```html
<!DOCTYPE html>
<html lang="en">
<head>
<meta charset="utf-8">
<title>Brightwater Advisory – Business Cards</title>
<link rel="stylesheet" href="https://fonts.googleapis.com/css2?family=Crimson+Text:wght@400;600&family=Josefin+Sans:wght@300;400&display=swap">
<style>
  :root {
    --backdrop: #d6d6d4;
    --card: #121212;
    --gold: #d9a21f;
    --white: #f2f2f2;
    --grey: #9a9a9a;
  }
  html, body {
    margin: 0;
    padding: 0;
    overflow: hidden;
  }
  .canvas {
    width: 1200px;
    height: 873px;
    background: var(--backdrop);
    display: flex;
    align-items: center;
    justify-content: center;
    gap: 60px;
  }
  .card {
    position: relative;
    width: 500px;
    height: 300px;
    background: var(--card);
    box-shadow: 0 6px 18px rgba(0,0,0,0.25);
    overflow: hidden;
  }

  /* Contact side */
  .person {
    position: absolute;
    top: 40px;
    right: 60px;
    text-align: left;
  }
  .person-name {
    font-family: "Josefin Sans", sans-serif;
    font-weight: 400;
    font-size: 26px;
    color: var(--gold);
    margin: 0;
  }
  .person-title {
    font-family: "Josefin Sans", sans-serif;
    font-weight: 300;
    font-size: 17px;
    color: var(--white);
    margin: 10px 0 0 4px;
    letter-spacing: 1px;
  }
  .contact-block {
    position: absolute;
    left: 44px;
    top: 116px;
  }
  .contact-list {
    margin: 0;
    padding: 0;
    list-style: none;
  }
  .contact-item {
    display: flex;
    align-items: center;
    gap: 16px;
    height: 30px;
    margin-bottom: 2px;
    font-family: "Josefin Sans", sans-serif;
    font-weight: 300;
    font-size: 16px;
    color: var(--gold);
    white-space: nowrap;
  }
  .contact-icon {
    width: 24px;
    height: 24px;
    flex: none;
  }
  .address-line {
    margin: 6px 0 0;
    font-family: "Josefin Sans", sans-serif;
    font-weight: 300;
    font-size: 16px;
    line-height: 1.35;
    color: var(--gold);
    font-style: normal;
    white-space: nowrap;
  }

  /* Logo side */
  .brand {
    position: absolute;
    left: 62px;
    top: 96px;
    display: flex;
    align-items: flex-start;
    gap: 18px;
  }
  .brand-square {
    width: 62px;
    height: 62px;
    border: 4px solid var(--white);
    box-sizing: border-box;
    flex: none;
    margin-top: -16px;
  }
  .brand-text {
    display: flex;
    flex-direction: column;
  }
  .brand-name {
    font-family: "Crimson Text", serif;
    font-weight: 400;
    font-size: 30px;
    letter-spacing: 2px;
    color: var(--white);
    margin: 0;
    line-height: 1.15;
    text-transform: uppercase;
  }
  .brand-rule {
    width: 320px;
    height: 2px;
    background: var(--gold);
    margin: 6px 0 8px;
  }
  .brand-tagline {
    font-family: "Josefin Sans", sans-serif;
    font-weight: 300;
    font-size: 9px;
    letter-spacing: 1.2px;
    color: var(--grey);
    text-transform: uppercase;
    margin: 0;
  }
</style>
</head>
<body>
<main class="canvas">

  <section class="card card-contact">
    <div class="person">
      <h1 class="person-name">Daniel Hart</h1>
      <p class="person-title">C.E.O.</p>
    </div>

    <div class="contact-block">
      <ul class="contact-list">
        <li class="contact-item">
          <svg class="contact-icon" viewBox="0 0 24 24" aria-hidden="true">
            <rect x="1" y="1" width="22" height="22" fill="none" stroke="#f2f2f2" stroke-width="2"/>
            <path d="M8 6 L10 6 L11 9 L9.5 10.5 C10.3 12 11.8 13.6 13.5 14.5 L15 13 L18 14 L18 16 C18 17 17 18 16 18 C10.5 17.5 6.5 13.5 6 8 C6 7 7 6 8 6 Z" fill="none" stroke="#d9a21f" stroke-width="1.3"/>
          </svg>
          +0123 987 654
        </li>
        <li class="contact-item">
          <svg class="contact-icon" viewBox="0 0 24 24" aria-hidden="true">
            <rect x="1" y="1" width="22" height="22" fill="none" stroke="#f2f2f2" stroke-width="2"/>
            <circle cx="12" cy="12" r="2.6" fill="none" stroke="#d9a21f" stroke-width="1.4"/>
            <path d="M14.6 12 L14.6 13.5 C14.6 15.5 17.5 15.5 17.5 12 A5.5 5.5 0 1 0 14.5 16.8" fill="none" stroke="#d9a21f" stroke-width="1.4"/>
          </svg>
          hello@brightwater.net
        </li>
        <li class="contact-item">
          <svg class="contact-icon" viewBox="0 0 24 24" aria-hidden="true">
            <rect x="1" y="1" width="22" height="22" fill="none" stroke="#f2f2f2" stroke-width="2"/>
            <circle cx="12" cy="12" r="6" fill="none" stroke="#d9a21f" stroke-width="1.3"/>
            <ellipse cx="12" cy="12" rx="2.6" ry="6" fill="none" stroke="#d9a21f" stroke-width="1.1"/>
            <path d="M6 12 H18 M7 9 H17 M7 15 H17" stroke="#d9a21f" stroke-width="1"/>
          </svg>
          www.brightwater-demo.com.au
        </li>
        <li class="contact-item">
          <svg class="contact-icon" viewBox="0 0 24 24" aria-hidden="true">
            <rect x="1" y="1" width="22" height="22" fill="none" stroke="#f2f2f2" stroke-width="2"/>
            <path d="M12 19 C9 15 7.5 12.5 7.5 10.5 A4.5 4.5 0 0 1 16.5 10.5 C16.5 12.5 15 15 12 19 Z" fill="none" stroke="#d9a21f" stroke-width="1.3"/>
            <circle cx="12" cy="10.5" r="1.6" fill="#d9a21f"/>
          </svg>
          Quarry Road 48,
        </li>
      </ul>
      <address class="address-line">4567 Harbourside, Australia</address>
    </div>
  </section>

  <section class="card card-brand">
    <div class="brand">
      <div class="brand-square" aria-hidden="true"></div>
      <div class="brand-text">
        <h2 class="brand-name">Brightwater<br>Advisory</h2>
        <div class="brand-rule" aria-hidden="true"></div>
        <p class="brand-tagline">Helping business to discover sustainable value</p>
      </div>
    </div>
  </section>

</main>
</body>
</html>
```